Name Card Design

Looking to create a card for my business. I am a personal stylist, my business is clothes, shoes and everything to do with looking fashion forward. I help people achieve the most polished look with cloths and grooming. I would like my card to be a reflection of my qualities which are: poise, elegance, creativity and fairness.
Things I like a simple yet expensive looking, sometimes less simple but highly creative and different catches my eye. For instance I saw a card with lace trimming at the bottom, it made me think about the business that person was in. I don't like childish designs with butterflies, trees, flowers, etc.
Here is my site www.Marta-Vosel.example for your perusal

On the card it should have the following info
Marta Vosel
personal stylist
www.Marta-Vosel.example
(+65) 482-30857
Facebook page: Ringthelook

Back of the card:
Wardrobe weeding
Personal shopping
Style consultation

Target Market(s)

mostly working women

Industry/Entity Type

Fashion

Font styles to use
Serif
Sans Serif

Requirements
Should not have
• butterflies, flowers, feathers, etc

```html
<!DOCTYPE html>
<html lang="en">
<head>
<meta charset="utf-8">
<title>Marta Vosel – Personal Stylist Business Card</title>
<link rel="stylesheet" href="https://fonts.googleapis.com/css2?family=Cinzel:wght@400;600;700&family=Lato:wght@400&display=swap">
<style>
  :root {
    --backdrop: #4b4b4d;
    --card-white: #ffffff;
    --brand-red: #bf2d27;
    --ink-black: #0d0d0d;
    --band-black: #000000;
    --photo-deep: #8a1e1a;
    --photo-mid: #c23a32;
    --photo-light: #d8574c;
  }
  * { margin: 0; padding: 0; box-sizing: border-box; }
  html, body {
    width: 1200px;
    height: 1000px;
    overflow: hidden;
    background: var(--backdrop);
  }
  .canvas {
    position: relative;
    width: 1200px;
    height: 1000px;
  }
  .card {
    position: absolute;
    width: 599px;
    height: 350px;
    background: var(--card-white);
    overflow: hidden;
  }
  /* Front: services side */
  .card--services { left: 171px; top: 127px; }
  .services__photo {
    position: absolute;
    left: 0; top: 0;
    width: 100%; height: 221px;
    background: linear-gradient(90deg, var(--photo-deep) 0%, var(--photo-mid) 35%, var(--photo-light) 60%, var(--photo-mid) 85%, var(--photo-deep) 100%);
  }
  .services__band {
    position: absolute;
    left: 0; top: 221px;
    width: 100%; height: 22px;
    background: var(--band-black);
  }
  .services__list {
    position: absolute;
    left: 0; top: 243px;
    width: 100%; height: 107px;
    display: flex;
    flex-direction: column;
    justify-content: center;
    align-items: center;
    gap: 6px;
    font-family: "Cinzel", serif;
    font-weight: 600;
    font-size: 19px;
    color: var(--ink-black);
    letter-spacing: 0.5px;
  }
  /* Back: contact side */
  .card--contact { left: 413px; top: 518px; }
  .contact__band {
    position: absolute;
    left: 0; top: 0;
    width: 100%; height: 19px;
    background: var(--band-black);
  }
  .contact__header {
    position: absolute;
    left: 0; top: 19px;
    width: 100%; height: 114px;
    background: var(--brand-red);
    text-align: center;
  }
  .contact__name {
    margin-top: 24px;
    font-family: "Cinzel", serif;
    font-weight: 400;
    font-size: 40px;
    line-height: 1;
    color: var(--ink-black);
    letter-spacing: 0.5px;
  }
  .contact__role {
    margin-top: 4px;
    font-family: "Lato", sans-serif;
    font-size: 20px;
    color: var(--card-white);
    letter-spacing: 2px;
  }
  .contact__details {
    position: absolute;
    left: 0; top: 133px;
    width: 100%; height: 217px;
    list-style: none;
    display: flex;
    flex-direction: column;
    justify-content: center;
    align-items: center;
    gap: 10px;
    padding-bottom: 12px;
  }
  .contact__item {
    font-family: "Lato", sans-serif;
    font-size: 19px;
    color: var(--ink-black);
  }
  .contact__label {
    font-family: "Cinzel", serif;
    font-weight: 700;
    color: var(--brand-red);
    margin-right: 4px;
  }
</style>
</head>
<body>
<main class="canvas">
  <section class="card card--services">
    <div class="services__photo" role="img" aria-label="Photograph of three women in fashionable outfits sitting in windows of a red wall, each holding an umbrella"></div>
    <div class="services__band"></div>
    <div class="services__list">
      <p>Wardrobe Weeding |Personal Shopping</p>
      <p>Style Consultation</p>
    </div>
  </section>

  <section class="card card--contact">
    <div class="contact__band"></div>
    <header class="contact__header">
      <h1 class="contact__name">MARTA VOSEL</h1>
      <p class="contact__role">PERSONAL STYLIST</p>
    </header>
    <ul class="contact__details">
      <li class="contact__item"><span class="contact__label">Mobile:</span>(+65) 482-30857</li>
      <li class="contact__item"><span class="contact__label">Email:</span>stylist@marta-vosel.example</li>
      <li class="contact__item"><span class="contact__label">Web:</span>www.Marta-Vosel.example</li>
      <li class="contact__item"><span class="contact__label">Facebook:</span>Ringthelook</li>
    </ul>
  </section>
</main>
</body>
</html>
```